Varek services highend custom homes

We build high end custom homes and timber frames we specialize in rustic hand made designs along with iron and concrete accents to add a modern touch 90% of my homes are buit on lake front properries attached is my logo and slogan as of now and my previous one

Target Market(s)

High end custom homes

Industry/Entity Type

Custom residential construction

Contact Information for Business Card

Been in buissness 8+ years inssured and reliable

Colors
A7469A
B969AE
D3A5CF
EDDBEB
F8F0F9

Requirements
Must have
• Must have slogan and phone number
Should not have
• A combination of rustic yet modern accents

```html
<!DOCTYPE html>
<html lang="en">
<head>
<meta charset="utf-8">
<title>Varek Services – Business Card</title>
<link href="https://fonts.googleapis.com/css2?family=Open+Sans:wght@300;400;700;800&family=Montserrat:wght@400&display=swap" rel="stylesheet">
<style>
  :root {
    --forest: #4e5d4a;
    --paper: #ffffff;
    --ink: #5a5a5a;
    --edge: #4a4a4a;
    --shade: rgba(60, 62, 40, 0.28);
  }
  * { margin: 0; padding: 0; box-sizing: border-box; }
  html, body {
    width: 1200px; height: 1200px; overflow: hidden;
    background: var(--paper);
    font-family: "Open Sans", Arial, sans-serif;
  }
  .sheet { position: relative; width: 1200px; height: 1200px; }

  .side-label {
    position: absolute; top: 370px; width: 500px;
    text-align: center; font-size: 34px; font-weight: 400; color: var(--ink);
  }
  .side-label--front { left: 88px; }
  .side-label--back { left: 629px; }

  .card {
    position: absolute; top: 433px; width: 500px; height: 321px;
    border-radius: 28px; overflow: hidden;
    box-shadow: 0 22px 18px -14px var(--shade);
  }
  .card--front { left: 88px; background: var(--paper); border: 1px solid var(--edge); }
  .card--back { left: 629px; background: var(--forest); }

  .name-band {
    position: absolute; left: 259px; top: 37px; width: 245px; height: 58px;
    background: var(--forest); border-radius: 29px 0 0 29px;
    color: var(--paper); text-align: right; padding-right: 29px;
  }
  .name-band__name { font-size: 20px; font-weight: 700; letter-spacing: 0.3px; line-height: 1; margin-top: 11px; }
  .name-band__role { font-size: 15px; font-weight: 300; line-height: 1; margin-top: 6px; }

  .brand { position: absolute; text-align: center; }
  .brand__mark { background: var(--forest); margin: 0 auto; }
  .brand__name { font-weight: 800; line-height: 1; white-space: nowrap; }
  .brand__slogan { font-weight: 400; letter-spacing: 0.3px; white-space: nowrap; }

  .brand--front { left: 40px; top: 160px; width: 180px; color: var(--forest); }
  .brand--front .brand__mark { width: 70px; height: 70px; }
  .brand--front .brand__name { font-size: 17px; margin-top: 22px; }
  .brand--front .brand__slogan { font-size: 9px; margin-top: 5px; }

  .divider {
    position: absolute; left: 233px; top: 150px; width: 2px; height: 140px;
    background: var(--forest); border-radius: 1px;
  }

  .contact-row { position: absolute; left: 256px; display: flex; align-items: center; }
  .contact-row__icon { width: 24px; height: 24px; fill: var(--forest); margin-right: 13px; flex: none; }
  .contact-row__text { font-size: 16px; line-height: 20px; color: var(--ink); white-space: nowrap; }
  .contact-row--phone { top: 144px; }
  .contact-row--mail { top: 198px; }
  .contact-row--place { top: 257px; }

  .brand--back { left: 0; top: 78px; width: 100%; color: var(--paper); }
  .brand--back .brand__mark { width: 100px; height: 100px; background: var(--paper); }
  .brand--back .brand__name { font-size: 24px; margin-top: 16px; }
  .brand--back .brand__slogan { font-size: 12px; margin-top: 6px; }

  .website {
    position: absolute; left: 0; top: 274px; width: 100%;
    display: flex; justify-content: center; align-items: center;
    font-family: "Montserrat", Arial, sans-serif; font-size: 15px;
    letter-spacing: 3.4px; color: var(--paper);
  }
  .website__icon { width: 14px; height: 14px; margin-right: 7px; }
</style>
</head>
<body>
<main class="sheet">
  <p class="side-label side-label--front">Front side</p>
  <p class="side-label side-label--back">Back side</p>

  <section class="card card--front" aria-label="Business card front">
    <div class="name-band">
      <p class="name-band__name">YOUR NAME HERE</p>
      <p class="name-band__role">Designation</p>
    </div>

    <div class="brand brand--front">
      <div class="brand__mark"></div>
      <p class="brand__name">VAREK SERVICES</p>
      <p class="brand__slogan">• BUILT FOR THE LAKESHORE •</p>
    </div>

    <div class="divider"></div>

    <div class="contact-row contact-row--phone">
      <svg class="contact-row__icon" viewBox="0 0 24 24" aria-hidden="true">
        <path d="M6.6 3.5l2.6 3.4-1.6 2a13 13 0 0 0 7.5 7.5l2-1.6 3.4 2.6-1.6 3A3 3 0 0 1 16 21 14 14 0 0 1 3 8a3 3 0 0 1 .6-2.9z"/>
      </svg>
      <p class="contact-row__text">+000-12345-6789<br>+000-12345-6789</p>
    </div>

    <div class="contact-row contact-row--mail">
      <svg class="contact-row__icon" viewBox="0 0 24 24" aria-hidden="true">
        <path d="M4 7h16l-8 6z"/>
        <path d="M4 9l8 6 8-6v9H4z"/>
      </svg>
      <p class="contact-row__text">e-mail@mail.com<br>e-mail@mail.com</p>
    </div>

    <div class="contact-row contact-row--place">
      <svg class="contact-row__icon" viewBox="0 0 24 24" aria-hidden="true">
        <path d="M12 2a7 7 0 0 0-7 7c0 5 7 13 7 13s7-8 7-13a7 7 0 0 0-7-7zm0 4a3 3 0 1 1 0 6 3 3 0 0 1 0-6z" fill-rule="evenodd"/>
      </svg>
      <p class="contact-row__text">Your Address<br>here 0123456</p>
    </div>
  </section>

  <section class="card card--back" aria-label="Business card back">
    <div class="brand brand--back">
      <div class="brand__mark"></div>
      <p class="brand__name">VAREK SERVICES</p>
      <p class="brand__slogan">• BUILT FOR THE LAKESHORE •</p>
    </div>

    <p class="website">
      <svg class="website__icon" viewBox="0 0 24 24" aria-hidden="true" fill="none" stroke="#ffffff" stroke-width="2">
        <circle cx="12" cy="12" r="10"/>
        <ellipse cx="12" cy="12" rx="4.5" ry="10"/>
        <path d="M2 12h20M4 7h16M4 17h16"/>
      </svg>
      www.yourweb.com
    </p>
  </section>
</main>
</body>
</html>
```